MS Word Template needed for a company specialized in network and security infrastructures

We need a new MS Word Template. <br/>Our activity is services in IT (network infrastructure and security). We usually use french language. <br/>The template must be nice and beautiful, and easy to use. If possible, try to use as less as possible text zones to simplify redaction tasks. And try to use "native" polices in MS Word. I attached sample documents for example. Please try to use the same colour codes.

Target Market(s)

Consulting in Network and security domain

Industry/Entity Type

It Service

Colors

Designer to choose colors to be used in the design.

Requirements
Must have
• - Nice design
• - Easy to use
• - very professional aspect
Nice to have
• - actual kelto arch systems logo
• - actual colour code

```html
<!DOCTYPE html>
<html lang="en">
<head>
<meta charset="utf-8">
<title>Kelto Arch Systems – Letterhead</title>
<link rel="stylesheet" href="https://fonts.googleapis.com/css2?family=Montserrat:wght@500;600;700&family=Jost:wght@500;600&display=swap">
<style>
  :root {
    --canvas: #ffffff;
    --header-band: #e8ebea;
    --page: #f6f8f9;
    --brand-green: #8ee57e;
    --brand-teal: #40c6bd;
    --contact: #3fc3b4;
    --headline: #2b5f63;
    --body-text: #2a2d30;
    --muted: #9aa5a6;
    --signature: #1f2a44;
    --swoosh-grey: #e7ecec;
  }
  * { margin: 0; padding: 0; box-sizing: border-box; }
  html, body {
    width: 1200px; height: 1089px; overflow: hidden;
    background: var(--canvas);
  }
  .letterhead {
    position: absolute; left: 204px; top: 0;
    width: 663px; height: 935px;
    background: linear-gradient(180deg, var(--page) 0%, #ffffff 60%, var(--page) 100%);
    overflow: hidden;
    font-family: "Montserrat", sans-serif;
  }
  .header-band {
    position: absolute; left: 0; top: 0; width: 100%; height: 261px;
    background: var(--header-band);
  }
  .brand {
    position: absolute; left: 74px; top: 110px;
    display: flex; align-items: center; gap: 14px;
  }
  .brand-dot {
    width: 34px; height: 34px; border-radius: 50%;
    background: var(--brand-teal);
  }
  .brand-name {
    font-weight: 600; font-size: 21px; letter-spacing: 1px;
    color: var(--brand-teal); text-transform: uppercase; line-height: 1;
  }
  .contact-list {
    position: absolute; left: 413px; top: 80px;
    list-style: none;
    font-family: "Jost", sans-serif; font-weight: 600;
    font-size: 12px; line-height: 15px; color: var(--contact);
  }
  .contact-item { display: flex; gap: 10px; margin-bottom: 8px; }
  .contact-icon { width: 14px; height: 14px; flex: none; margin-top: 1px; fill: var(--contact); }
  .subject {
    position: absolute; left: 72px; top: 324px;
    font-weight: 700; font-size: 24px; letter-spacing: 0.3px;
    color: var(--headline);
  }
  .letter-body {
    position: absolute; left: 72px; top: 386px; width: 520px;
    font-weight: 500; font-size: 12.6px; line-height: 16px;
    color: var(--body-text);
    text-align: justify; text-align-last: justify;
  }
  .letter-body p + p { margin-top: 31px; }
  .sign-off {
    position: absolute; right: 75px; top: 740px;
    text-align: right; font-family: "Jost", sans-serif; font-weight: 600;
  }
  .sign-role { font-size: 12.5px; color: var(--muted); line-height: 18px; }
  .sign-note { font-size: 12.5px; color: var(--signature); line-height: 18px; }
  .sign-web { font-size: 11.5px; color: var(--muted); line-height: 18px; font-weight: 500; }
  .footer-waves { position: absolute; left: 0; top: 0; width: 663px; height: 935px; }
</style>
</head>
<body>
  <main class="letterhead">
    <div class="header-band"></div>

    <div class="brand">
      <span class="brand-dot"></span>
      <span class="brand-name">Kelto Arch Systems</span>
    </div>

    <ul class="contact-list">
      <li class="contact-item">
        <svg class="contact-icon" viewBox="0 0 14 14"><path d="M1 3h12v8H1z" /><path d="M1 3l6 4.5L13 3" fill="none" stroke="#e8ebea" stroke-width="1.2"/></svg>
        <span>info@keltoarchmail</span>
      </li>
      <li class="contact-item">
        <svg class="contact-icon" viewBox="0 0 14 14"><path d="M7 0.5a4.5 4.5 0 0 0-4.5 4.5C2.5 8.5 7 13.5 7 13.5S11.5 8.5 11.5 5A4.5 4.5 0 0 0 7 0.5zm0 6.3a1.8 1.8 0 1 1 0-3.6 1.8 1.8 0 0 1 0 3.6z"/></svg>
        <span>Sample Lane 48b<br>Town Quarter, City, Zone</span>
      </li>
      <li class="contact-item">
        <svg class="contact-icon" viewBox="0 0 14 14"><path d="M3 1l2.4 2.8-1.3 1.6a8 8 0 0 0 4.5 4.5l1.6-1.3L13 11l-1.6 2C6 13 1 8 1 2.6z"/></svg>
        <span>+00 4321 8765 2109<br>+00 4321 8765 2109</span>
      </li>
    </ul>

    <h1 class="subject">SUBJECT HEALINE HERE</h1>

    <div class="letter-body">
      <p>Lorem ipsum dolor sit amet, consectetur adipiscing elit. Donec diam nisi, sodales eu condimentum eget, blandit ac ex. Nunc sit amet diam lacinia sem finibus suscipit. Nunc consectetur euismod turpis, quis porttitor massa lobortis eget. Integer mollis sed lectus et pellentesque. Proin volutpat augue quis eros tristique blandit. Quisque et pellentesque arcu. Vestibulum eget lacus sollicitu-din mi suscipit fermentum. Curabitur quis nunc odio.</p>
      <p>Lorem ipsum dolor sit amet, consectetur adipiscing elit. Donec diam nisi, sodales eu condimentum eget, blandit ac ex. Nunc sit amet diam lacinia sem finibus suscipit. Nunc consectetur euismod turpis, quis porttitor massa lobortis eget. Integer mollis sed lectus et pellentesque. Proin volutpat augue quis eros tristique blandit. Quisque et pellentesque arcu. Vestibulum eget lacus sollicitu-din mi suscipit fermentum. Curabitur quis nunc odio.</p>
    </div>

    <div class="sign-off">
      <p class="sign-role">Creative Art Director</p>
      <p class="sign-note">Pellentesque id neque ligula. Nullam posuere</p>
      <p class="sign-web">www.yourfirmname</p>
    </div>

    <svg class="footer-waves" viewBox="0 0 596 842" preserveAspectRatio="none" aria-hidden="true">
      <path d="M0,668 Q250,800 596,712 L596,842 L0,842 Z" fill="var(--swoosh-grey)"/>
      <path d="M0,708 Q290,858 596,718 L596,842 L0,842 Z" fill="var(--brand-green)"/>
      <path d="M0,752 Q300,832 596,730 L596,842 L0,842 Z" fill="var(--brand-teal)"/>
    </svg>
  </main>
</body>
</html>
```